Visitenkarte erstellen für Reiki Praxis

Visitenkarten für Reiki Praxis Doppelseitig

business cards reiki practice double-sided

The background can also be a different color

```html
<!DOCTYPE html>
<html lang="en">
<head>
<meta charset="utf-8">
<title>Serene Currents – Business Card</title>
<link rel="stylesheet" href="https://fonts.googleapis.com/css2?family=Montserrat:wght@400;500&display=swap">
<style>
  :root {
    --page-bg: #ebe6e0;
    --card-white: #ffffff;
    --ink: #1b1b1b;
    --text-light: #ffffff;
    --grad-sand: #c9a684;
    --grad-sage: #9c9f8f;
    --grad-mauve: #a8728b;
    --card-shadow: rgba(0, 0, 0, 0.28);
  }
  html, body {
    margin: 0;
    padding: 0;
    width: 900px;
    height: 1200px;
    overflow: hidden;
    background: var(--page-bg);
    font-family: "Montserrat", sans-serif;
  }
  .canvas {
    position: relative;
    width: 900px;
    height: 1200px;
  }
  .card {
    position: absolute;
    left: 80px;
    width: 742px;
    height: 440px;
    border-radius: 40px;
    overflow: hidden;
    box-shadow: 0 6px 14px var(--card-shadow);
  }
  .card-front { top: 132px; background: var(--card-white); }
  .card-back {
    top: 638px;
    background: linear-gradient(90deg, var(--grad-sand) 0%, var(--grad-sage) 45%, var(--grad-mauve) 100%);
  }

  /* Front: brand area */
  .brand-front {
    position: absolute;
    top: 0; left: 0; right: 0;
    height: 236px;
    display: flex;
    flex-direction: column;
    align-items: center;
    justify-content: flex-end;
    padding-bottom: 28px;
    box-sizing: border-box;
    color: var(--ink);
    font-weight: 500;
    text-align: center;
  }
  .brand-front .brand-name { font-size: 34px; letter-spacing: 0.5px; line-height: 1.1; }
  .brand-front .brand-owner { font-size: 22px; letter-spacing: 5px; margin-top: 6px; }

  .rule {
    position: absolute;
    top: 238px; left: 0; right: 0;
    height: 4px;
    background: var(--ink);
  }
  .contact-band {
    position: absolute;
    top: 246px; left: 0; right: 0; bottom: 0;
    background: linear-gradient(90deg, var(--grad-sand) 0%, var(--grad-sage) 45%, var(--grad-mauve) 100%);
    color: var(--text-light);
  }
  .person {
    position: absolute;
    right: 425px;
    top: 50px;
    text-align: right;
  }
  .person-name { font-size: 23px; font-weight: 500; }
  .person-title { font-size: 15px; margin-top: 6px; }
  .divider {
    position: absolute;
    left: 376px;
    top: 50px;
    width: 2px;
    height: 62px;
    background: var(--text-light);
  }
  .contact-list {
    position: absolute;
    left: 422px;
    top: 39px;
    margin: 0;
    padding: 0;
    list-style: none;
    font-size: 16px;
  }
  .contact-list li {
    display: flex;
    align-items: center;
    height: 27px;
  }
  .contact-list svg { width: 16px; height: 16px; margin-right: 12px; fill: var(--text-light); }
  .address {
    position: absolute;
    left: 0; right: 0;
    top: 146px;
    text-align: center;
    font-size: 15px;
  }

  /* Back */
  .brand-back {
    position: absolute;
    left: 0; right: 0;
    top: 252px;
    text-align: center;
    color: var(--text-light);
    font-weight: 400;
  }
  .brand-back .brand-name { font-size: 48px; letter-spacing: 1px; line-height: 1.1; }
  .brand-back .brand-owner { font-size: 32px; letter-spacing: 7px; margin-top: 6px; }
</style>
</head>
<body>
<main class="canvas">
  <section class="card card-front" aria-label="Business card front">
    <div class="brand-front">
      <div class="brand-name">SERENE CURRENTS</div>
      <div class="brand-owner">MARA VELDEN</div>
    </div>
    <div class="rule"></div>
    <div class="contact-band">
      <div class="person">
        <div class="person-name">Daniel Reyes</div>
        <div class="person-title">CEO &amp; Founder</div>
      </div>
      <div class="divider"></div>
      <ul class="contact-list">
        <li>
          <svg viewBox="0 0 24 24" aria-hidden="true"><path d="M6.6 10.8a15.1 15.1 0 0 0 6.6 6.6l2.2-2.2a1 1 0 0 1 1-.25 11.4 11.4 0 0 0 3.6.57 1 1 0 0 1 1 1V20a1 1 0 0 1-1 1A17 17 0 0 1 3 4a1 1 0 0 1 1-1h3.5a1 1 0 0 1 1 1c0 1.25.2 2.45.57 3.57a1 1 0 0 1-.25 1z"/></svg>
          1-800-555-0142
        </li>
        <li>
          <svg viewBox="0 0 24 24" aria-hidden="true"><path d="M3 6h18v2l-9 5.5L3 8z"/><path d="M3 10l9 5.5 9-5.5v8H3z"/></svg>
          info@yourmail.com
        </li>
        <li>
          <svg viewBox="0 0 24 24" aria-hidden="true"><path d="M12 2a10 10 0 1 0 0 20 10 10 0 0 0 0-20zm-1 17.9A8 8 0 0 1 4.2 10.5L9 15v1a2 2 0 0 0 2 2zm6.9-2.5A2 2 0 0 0 16 16h-1v-3a1 1 0 0 0-1-1H8v-2h2a1 1 0 0 0 1-1V7h2a2 2 0 0 0 2-2v-.4a8 8 0 0 1 2.9 12.8z"/></svg>
          www.yourwebsite.com
        </li>
      </ul>
      <div class="address">48 Willow Bend Road, Fairhaven NY 11000</div>
    </div>
  </section>

  <section class="card card-back" aria-label="Business card back">
    <div class="brand-back">
      <div class="brand-name">SERENE CURRENTS</div>
      <div class="brand-owner">MARA VELDEN</div>
    </div>
  </section>
</main>
</body>
</html>
```